TAILWIND FIELDS Pet Resorts Outdoor Signage

4 x 8 outdoor signage design for our two locations

Target Market(s)

Existing and New Customers

Industry/Entity Type

Pet Care

Font styles to use
Sans Serif

Colors

Designer to choose colors to be used in the design.

```html
<!DOCTYPE html>
<html lang="en">
<head>
<meta charset="UTF-8">
<title>Tailwind Fields Pet Resorts – Outdoor Sign</title>
<link rel="stylesheet" href="https://fonts.googleapis.com/css2?family=Jost:wght@400;600;700&family=Roboto+Condensed:wght@700&display=swap">
<style>
  :root {
    --navy: #1a1042;
    --orange: #f8aa4b;
    --white: #ffffff;
    --page: #ffffff;
  }
  * { margin: 0; padding: 0; box-sizing: border-box; }
  html, body { width: 1200px; height: 1200px; overflow: hidden; background: var(--page); }
  .canvas { position: relative; width: 1200px; height: 1200px; border: 1px solid #444; }
  .sign {
    position: absolute; left: 333px; top: 67px; width: 533px; height: 1065px;
    background: var(--navy); overflow: hidden;
  }
  .sign-title {
    position: absolute; left: 50%; top: 44px;
    transform: translateX(-50%) scaleX(0.85); transform-origin: center top;
    white-space: nowrap;
    font-family: "Jost", sans-serif; font-weight: 700;
    font-size: 96px; line-height: 1; color: var(--orange);
  }
  .tagline-band {
    position: absolute; left: 1px; top: 178px; width: 532px; height: 63px;
    background: var(--white); display: flex; align-items: center; justify-content: center;
  }
  .tagline {
    font-family: "Roboto Condensed", sans-serif; font-weight: 700;
    font-size: 40px; color: var(--navy); line-height: 1; letter-spacing: 0.3px;
    white-space: nowrap;
  }
  .brand-name {
    position: absolute; left: 0; top: 385px; width: 100%;
    text-align: center; font-family: "Jost", sans-serif; font-weight: 700;
    color: var(--orange); line-height: 1; white-space: nowrap;
  }
  .brand-name .line-1 { display: block; font-size: 92px; }
  .brand-name .line-2 { display: block; font-size: 128px; }
  .service {
    position: absolute; display: flex; align-items: center;
    font-family: "Roboto Condensed", sans-serif; font-weight: 700;
    font-size: 26px; color: var(--white); line-height: 1; white-space: nowrap;
  }
  .service-dot {
    width: 31px; height: 31px; border-radius: 50%; background: var(--orange);
    margin-right: 9px; flex: none;
  }
  .contact-bar-left {
    position: absolute; left: 0; top: 927px; width: 161px; height: 79px; background: var(--orange);
  }
  .contact-bar-right {
    position: absolute; right: 0; top: 927px; width: 27px; height: 79px; background: var(--orange);
  }
  .phone {
    position: absolute; right: 46px; top: 926px;
    font-family: "Jost", sans-serif; font-weight: 600; font-size: 48px;
    color: var(--white); line-height: 1; letter-spacing: -1px; white-space: nowrap;
  }
  .website {
    position: absolute; right: 46px; top: 981px;
    font-family: "Jost", sans-serif; font-weight: 600; font-size: 18px;
    color: var(--white); line-height: 1; white-space: nowrap;
  }
</style>
</head>
<body>
<div class="canvas">
  <section class="sign">
    <h1 class="sign-title">PET RESORT</h1>
    <div class="tagline-band"><p class="tagline">ALL BREED FRIENDLY</p></div>

    <p class="brand-name"><span class="line-1">TAILWIND</span><span class="line-2">FIELDS</span></p>

    <p class="service" style="left:58px; top:793px;"><span class="service-dot"></span>Boarding</p>
    <p class="service" style="left:214px; top:793px;"><span class="service-dot"></span>Daycare</p>
    <p class="service" style="left:356px; top:793px;"><span class="service-dot"></span>Training</p>
    <p class="service" style="left:47px; top:844px;"><span class="service-dot"></span>Full-Service Salon</p>
    <p class="service" style="left:291px; top:844px;"><span class="service-dot"></span>Pet Taxi &amp; More</p>

    <div class="contact-bar-left"></div>
    <div class="contact-bar-right"></div>
    <p class="phone">905-555-0142</p>
    <p class="website">www.tailwindfields.ca</p>
  </section>
</div>
</body>
</html>
```